tamo rix

TAMO RIX mobile technology servicesPhone and tablet repairs, screens data recovery.

Industry/Entity Type

Data Recovery

Contact Information for Business Card

0431 587 612

Colors
33a6d7
f04a50
0a90cc
e34197

Requirements
Must have
• Gary plinth
Nice to have
• White background

```html
<!DOCTYPE html>
<html lang="en">
<head>
<meta charset="utf-8">
<title>Tamo Rix – Business Card</title>
<link rel="stylesheet" href="https://fonts.googleapis.com/css2?family=Arimo:wght@700&family=Michroma&display=swap">
<style>
  :root {
    --card-white: #ffffff;
    --panel-black: #000000;
    --ink: #000000;
    --name-blue: #33a6d7;
    --tag-white: #ffffff;
  }
  html, body {
    margin: 0;
    padding: 0;
    overflow: hidden;
    background: var(--card-white);
  }
  .card {
    position: relative;
    width: 1200px;
    height: 741px;
    background: var(--card-white);
    overflow: hidden;
  }
  .card__panel {
    position: absolute;
    inset: 0;
    width: 1200px;
    height: 741px;
  }
  .brand {
    position: absolute;
    left: 78px;
    top: 500px;
    width: 400px;
    text-align: center;
  }
  .brand__name {
    margin: 0;
    font-family: "Arimo", sans-serif;
    font-weight: 700;
    font-size: 40px;
    line-height: 1;
    letter-spacing: 1px;
    color: var(--tag-white);
  }
  .brand__tagline {
    margin: 12px 0 0;
    font-family: "Arimo", sans-serif;
    font-weight: 700;
    font-size: 17px;
    letter-spacing: 0.5px;
    color: var(--tag-white);
  }
  .contact {
    position: absolute;
    right: 60px;
    top: 296px;
    text-align: right;
  }
  .contact__name {
    margin: 0;
    font-family: "Arimo", sans-serif;
    font-weight: 700;
    font-size: 66px;
    line-height: 1;
    color: var(--name-blue);
  }
  .contact__phone {
    display: flex;
    align-items: center;
    justify-content: flex-end;
    gap: 14px;
    margin-top: 8px;
    font-family: "Arimo", sans-serif;
    font-weight: 700;
    font-size: 40px;
    letter-spacing: 5px;
    color: var(--ink);
  }
  .contact__icon {
    width: 44px;
    height: 54px;
  }
  .services {
    position: absolute;
    right: 60px;
    top: 592px;
    margin: 0;
    text-align: right;
    font-family: "Michroma", sans-serif;
    font-size: 27px;
    line-height: 42px;
    letter-spacing: 2px;
    color: var(--ink);
    -webkit-text-stroke: 0.8px var(--ink);
  }
</style>
</head>
<body>
  <main class="card">
    <svg class="card__panel" viewBox="0 0 1200 741" aria-hidden="true">
      <path d="M0 0 H502 Q630 370 425 741 H0 Z" fill="var(--panel-black)"/>
    </svg>

    <div class="brand">
      <p class="brand__name">Tamo Rix</p>
      <p class="brand__tagline">MOBILE TECHNOLOGY SERVICES</p>
    </div>

    <section class="contact">
      <h1 class="contact__name">Gary plinth</h1>
      <div class="contact__phone">
        <svg class="contact__icon" viewBox="0 0 44 54" aria-hidden="true">
          <g transform="rotate(-22 22 27)">
            <rect x="11" y="4" width="22" height="46" rx="4" fill="none" stroke="var(--ink)" stroke-width="3"/>
            <line x1="18" y1="44" x2="26" y2="44" stroke="var(--ink)" stroke-width="2.5" stroke-linecap="round"/>
          </g>
        </svg>
        <span class="contact__number">0431 587 612</span>
      </div>
    </section>

    <p class="services">PHONE &amp; TABLET REPAIRS<br>SCREENS DATA RECOVERY</p>
  </main>
</body>
</html>
```